Business card design and logo needed - Photographer

I take photos of weddings, rodeos, snowmobiling.
Need a card to hand out to prospective clients.
Industry/Entity Type
Business
Contact Information for Business Card
Marcus Dolven Photography
Requirements
Must have
- Bold
Black or white base.
My website. www.MarcusDolven.example
Should not have
- camera/ lens/ aperture blades

```html
<!DOCTYPE html>
<html lang="en">
<head>
<meta charset="utf-8">
<title>Marcus Dolven Photography – Business Card</title>
<link href="https://fonts.googleapis.com/css2?family=Saira:wght@400;500;600&display=swap" rel="stylesheet">
<style>
  :root {
    --backdrop: #8a8d8f;
    --card: #1c2021;
    --teal: #35c6ae;
    --ink: #ffffff;
  }
  html, body {
    margin: 0;
    width: 1200px;
    height: 900px;
    overflow: hidden;
    background: var(--backdrop);
  }
  .card {
    position: absolute;
    left: 75px;
    top: 150px;
    width: 1050px;
    height: 600px;
    background: var(--card);
    overflow: hidden;
    font-family: "Saira", sans-serif;
    color: var(--ink);
  }
  .card-accent {
    position: absolute;
    inset: 0;
  }
  .brand {
    position: absolute;
    left: 420px;
    top: 60px;
  }
  .brand-name {
    margin: 0;
    font-size: 66px;
    font-weight: 600;
    line-height: 0.95;
    letter-spacing: 1px;
  }
  .brand-name span { display: block; }
  .brand-name .surname { padding-left: 40px; }
  .brand-tagline {
    margin: 6px 0 0 120px;
    font-size: 34px;
    font-weight: 500;
    letter-spacing: 1px;
  }
  .contact {
    position: absolute;
    display: flex;
    align-items: center;
    gap: 16px;
    font-size: 26px;
    font-weight: 500;
    letter-spacing: 0.5px;
    white-space: nowrap;
  }
  .contact-email { left: 50px; top: 300px; }
  .contact-phone { right: 50px; top: 400px; }
  .contact-web {
    left: 50px;
    top: 540px;
    color: var(--card);
    font-weight: 600;
  }
  .contact-icon { width: 40px; height: 40px; flex: none; }
</style>
</head>
<body>
  <section class="card" aria-label="Marcus Dolven Photography business card">
    <svg class="card-accent" viewBox="0 0 1050 600" aria-hidden="true">
      <polygon points="0,370 230,470 1050,470 1050,492 222,492 0,394" fill="var(--teal)"/>
      <polygon points="0,440 180,520 1050,520 1050,600 0,600" fill="var(--teal)"/>
    </svg>

    <header class="brand">
      <h1 class="brand-name"><span class="given">Marcus</span><span class="surname">Dolven</span></h1>
      <p class="brand-tagline">photography</p>
    </header>

    <div class="contact contact-email">
      <svg class="contact-icon" viewBox="0 0 40 40" aria-hidden="true">
        <circle cx="20" cy="20" r="18" fill="none" stroke="var(--teal)" stroke-width="2"/>
        <rect x="10" y="13" width="20" height="14" fill="none" stroke="var(--teal)" stroke-width="2"/>
        <polyline points="10,13 20,21 30,13" fill="none" stroke="var(--teal)" stroke-width="2"/>
      </svg>
      <span>marcusdolven@example.com</span>
    </div>

    <div class="contact contact-phone">
      <svg class="contact-icon" viewBox="0 0 40 40" aria-hidden="true">
        <circle cx="20" cy="20" r="18" fill="none" stroke="var(--teal)" stroke-width="2"/>
        <path d="M14 11 l4 0 l2 5 l-3 2 q2 4 5 6 l2 -3 l5 2 l0 4 q-1 2 -4 2 q-10 -2 -13 -14 q0 -3 2 -4 z" fill="var(--teal)"/>
      </svg>
      <span>555 010 4827</span>
    </div>

    <div class="contact contact-web">
      <span>www.MarcusDolven.example</span>
    </div>
  </section>
</body>
</html>
```